I need a book cover for a Regency Romance.
I'd like a beautiful blonde, demure young woman who has just lowered her mask and is looking at the hero who is just out of the picture.

She is at a masquerade ball but so her costume is silvery white. The mask is made of pearls and white feathers

• Must have a romantic feel.
• The Title is: Velvet Promise
• Author's name: Corinne Halbrook
• Series name: Stray Sparrows of Thornwick Series
• Take a look at some of my prior covers. I am looking for something just as romantic and dramatic, suspenseful

```html
<!DOCTYPE html>
<html lang="en">
<head>
<meta charset="utf-8">
<title>Velvet Promise – Book Cover</title>
<link rel="stylesheet" href="https://fonts.googleapis.com/css2?family=Bodoni+Moda:wght@500;600&family=Cinzel:wght@400;600&family=EB+Garamond:wght@400;500&family=Great+Vibes&display=swap">
<style>
  :root {
    --backdrop: #e6e6e8;
    --cover-black: #060606;
    --silver-light: #f2f2f2;
    --silver-mid: #b9b9bb;
    --silver-dark: #7d7d80;
    --body-grey: #8a8a8a;
    --rule-grey: #a8a8a8;
    --art-dark: #0d0b0d;
    --art-plum: #5a2a4a;
    --art-rose: #b46d98;
    --art-skin: #6f5a52;
    --page-edge: #ece6d4;
  }
  * { box-sizing: border-box; margin: 0; padding: 0; }
  html, body { width: 1200px; height: 800px; overflow: hidden; }
  body {
    background: var(--backdrop);
    font-family: "EB Garamond", Georgia, serif;
    display: flex; align-items: center; justify-content: center;
  }
  .book-wrap { display: flex; height: 640px; box-shadow: 0 14px 40px rgba(0,0,0,.25); }

  .silver {
    background: linear-gradient(180deg, var(--silver-light) 0%, var(--silver-mid) 55%, var(--silver-dark) 100%);
    -webkit-background-clip: text; background-clip: text; color: transparent;
  }

  /* back cover */
  .back-cover {
    width: 420px; background: var(--cover-black); position: relative;
    padding: 22px 32px 0;
  }
  .back-author {
    font-family: "Cinzel", serif; font-size: 11px; letter-spacing: .5px;
    color: var(--silver-mid); text-align: right;
  }
  .back-title {
    font-family: "Bodoni Moda", serif; font-weight: 500; font-size: 46px;
    text-align: center; letter-spacing: 1px; transform: scaleY(1.2); margin-top: 8px; line-height: 1;
  }
  .series-line {
    display: flex; align-items: center; gap: 10px; margin-top: 12px;
    font-family: "Cinzel", serif; font-weight: 600; color: var(--silver-mid);
  }
  .series-line::before, .series-line::after {
    content: ""; flex: 1; height: 2px; background: var(--rule-grey);
  }
  .back-cover .series-line { font-size: 12px; }
  .blurb {
    margin-top: 18px; font-size: 11.4px; line-height: 1.42; color: var(--body-grey);
    text-align: justify; text-align-last: center;
  }
  .back-footer {
    position: absolute; left: 32px; right: 32px; bottom: 28px;
    display: flex; gap: 16px;
  }
  .back-footer span {
    flex: 1; height: 64px; border: 1px solid #1e1e1e;
    display: flex; align-items: center; justify-content: center;
    font-family: "Cinzel", serif; font-size: 10px; color: #555;
  }

  /* spine */
  .spine {
    width: 44px; background: var(--cover-black); border-left: 1px solid #1a1a1a; border-right: 1px solid #1a1a1a;
    display: flex; flex-direction: column; align-items: center; padding: 28px 0 36px;
  }
  .spine-text { writing-mode: vertical-rl; }
  .spine-title {
    font-family: "Bodoni Moda", serif; font-weight: 500; font-size: 30px; letter-spacing: 1px;
  }
  .spine-author {
    margin-top: auto; font-family: "Cinzel", serif; font-size: 10px; color: var(--silver-mid);
  }

  /* front cover */
  .front-cover {
    width: 420px; background: var(--cover-black); position: relative;
    display: flex; flex-direction: column;
  }
  .genre-line {
    font-family: "Cinzel", serif; font-size: 11px; letter-spacing: 5.2px;
    color: var(--silver-mid); text-align: center; padding-top: 8px;
  }
  .front-title {
    font-family: "Bodoni Moda", serif; font-weight: 600; font-size: 54px;
    text-align: center; letter-spacing: .5px; transform: scaleY(1.25);
    margin-top: 10px; line-height: 1;
  }
  .front-cover .series-line { font-size: 13.5px; margin: 22px 14px 0; }
  .cover-art {
    position: relative; margin-top: 14px; height: 440px;
    background:
      radial-gradient(ellipse at 78% 52%, var(--art-skin) 0%, transparent 38%),
      radial-gradient(ellipse at 22% 30%, var(--art-rose) 0%, var(--art-plum) 28%, transparent 55%),
      linear-gradient(90deg, #2a1524 0%, var(--art-dark) 60%, #050505 100%);
  }
  .tagline {
    position: absolute; top: 34px; right: 14px; transform: rotate(-6deg);
    font-family: "Great Vibes", cursive; font-size: 25px; color: #eee;
  }
  .front-author {
    margin-top: auto; padding-bottom: 14px; text-align: center;
    font-family: "EB Garamond", serif; font-weight: 500; font-size: 17px;
    letter-spacing: 1px; color: var(--silver-light);
  }
</style>
</head>
<body>
  <div class="book-wrap">
    <section class="back-cover">
      <p class="back-author">BY CORINNE HALBROOK</p>
      <h2 class="back-title silver">VELVET PROMISE</h2>
      <p class="series-line">THE STRAY SPARROWS OF THORNWICK SERIES</p>
      <p class="blurb">Lorem ipsum dolor sit amet, consectetur adipisicing elit, sed do eiusmod tempor incididunt ut labore et dolore magna aliqua. Ut enim ad minim veniam, quis nostrud exercitation. Lorem ipsum dolor sit amet, consectetur adipisicing elit, sed do eiusmod tempor incididunt ut labore et dolore magna aliqua. Ut enim ad minim veniam, quis nostrud exercitation. Lorem ipsum dolor sit amet, consectetur adipisicing elit, sed do eiusmod tempor incididunt ut labore et dolore magna aliqua. Ut enim ad minim veniam, quis nostrud exercitation. Lorem ipsum dolor sit amet, consectetur adipisicing elit, sed do eiusmod tempor incididunt ut labore et dolore magna aliqua. Ut enim ad minim veniam, quis nostrud exercitation. Lorem ipsum dolor sit amet, consectetur adipisicing elit, sed do eiusmod tempor incididunt ut labore et dolore magna aliqua. Ut enim ad minim veniam, quis nostrud exercitation. Lorem ipsum dolor sit amet, consectetur adipisicing elit, sed do eiusmod tempor incididunt ut labore et dolore magna aliqua. Ut enim ad minim veniam, quis nostrud exercitation. Lorem ipsum dolor sit amet, consectetur adipisicing elit, sed do eiusmod tempor incididunt ut labore et dolore magna aliqua. Ut enim ad minim veniam, quis nostrud exercitation.</p>
      <div class="back-footer"><span>LOGO</span><span>ISBN</span></div>
    </section>

    <div class="spine">
      <span class="spine-text spine-title silver">VELVET PROMISE</span>
      <span class="spine-text spine-author">BY CORINNE HALBROOK</span>
    </div>

    <section class="front-cover">
      <p class="genre-line">1800'S REGENCY ROMANCE</p>
      <h1 class="front-title silver">VELVET PROMISE</h1>
      <p class="series-line">THE STRAY SPARROWS OF THORNWICK SERIES</p>
      <div class="cover-art" role="img" aria-label="Painted illustration: a woman in a feathered pink and silver masquerade mask with red lips, and a dark-haired man leaning in close, his hand at her jaw, against a black background">
        <p class="tagline">Wrong kiss, Right heart</p>
      </div>
      <p class="front-author">BY CORINNE HALBROOK</p>
    </section>
  </div>
</body>
</html>
```